Vora Kest Cleansers Trading L.L.C

We need stationary design for our new company contain ( Business card - head latter - envelops( big & small) - folder file ) One identity and creative design & has related with logo colors ....A unified identity
The main elements of the design that includes the main logos (logo vora + vora logo membership Saif bin Harun) as it is in the attachment then the address of the company.
The Address is
Ras Kulaib - Next to Nuwar Plaza Mall
Fanar Trade Tower - 614
P.O.Box : 48207 Dubai - U.A.E
Tel. : 00971 4 57 86 204
Fax : 00971 4 57 86 205
Email : info@vorakestclean.example
www.vorakestclean.example
Please read the attachment in an important way, especially the terms of the government logo (Saif Bin Harun Membership)
In the design of business cards .. Please put slogans (Pivo green care - Pivo Professional - Khubrat ) be in the back of the card
Put my name sample
Sami Yousef Hamdan Jaber
Director Manager
Mobil : + 971 55 839 0 839

```html
<!DOCTYPE html>
<html lang="en">
<head>
<meta charset="utf-8">
<title>Vora Kest Cleansers Trading L.L.C — Stationery</title>
<link rel="stylesheet" href="https://fonts.googleapis.com/css2?family=Open+Sans:wght@400;600;700&display=swap">
<style>
  :root {
    --brand-blue: #3f6fb8;
    --brand-green: #80b841;
    --paper: #ffffff;
    --stage: #d9d9db;
    --ink: #4a4a4a;
    --rule: #d4d4d4;
  }
  * { margin: 0; padding: 0; box-sizing: border-box; }
  html, body { width: 1200px; height: 991px; overflow: hidden; }
  body { background: var(--stage); font-family: "Open Sans", sans-serif; color: var(--ink); }
  .canvas { position: relative; width: 1200px; height: 991px; overflow: hidden; }
  .sheet { position: absolute; background: var(--paper); overflow: hidden; }

  /* company name block: one colour, one weight */
  .mark { position: absolute; display: flex; align-items: center; }
  .mark-dot { border: 3px solid var(--brand-blue); border-radius: 50%; flex: none; }
  .mark-text { display: flex; flex-direction: column; color: var(--brand-blue); font-weight: 600; white-space: nowrap; }
  .mark-name { line-height: 1.05; }
  .mark-sub { text-transform: uppercase; }
  .on-blue .mark-text { color: var(--paper); }
  .on-blue .mark-dot { border-color: var(--paper); }

  /* letterhead */
  .letterhead { left: 71px; top: 104px; width: 398px; height: 560px; }
  .letterhead .mark { left: 35px; top: 38px; gap: 8px; }
  .letterhead .mark-dot { width: 34px; height: 34px; }
  .letterhead .mark-name { font-size: 22px; }
  .letterhead .mark-sub { font-size: 5.6px; margin-top: 2px; }
  .partner-row { position: absolute; left: 36px; right: 34px; top: 496px; display: flex; justify-content: space-between; align-items: center; }
  .partner-badge { width: 62px; height: 26px; border-radius: 3px; }
  .partner-badge.green { background: var(--brand-green); }
  .partner-badge.red { background: #d7473c; }
  .partner-badge.navy { background: #5b78b5; }
  .partner-badge.rose { background: #e07a86; }
  .partner-sep { width: 1px; height: 32px; background: var(--rule); }
  .letterhead-rule { position: absolute; left: 35px; right: 34px; top: 526px; height: 1px; background: var(--rule); }
  .letterhead-footer { position: absolute; left: 35px; right: 34px; top: 532px; display: flex; justify-content: space-between; font-size: 5.4px; line-height: 1.35; }
  .letterhead-footer b { color: var(--brand-green); font-weight: 600; }

  /* folder */
  .folder { left: 507px; top: 90px; width: 433px; height: 575px; background: var(--brand-blue); border-radius: 2px 6px 2px 2px; }
  .folder .mark { left: 150px; top: 70px; gap: 12px; }
  .folder .mark-dot { width: 60px; height: 60px; border-width: 4px; }
  .folder .mark-name { font-size: 36px; }
  .folder .mark-sub { font-size: 9.5px; margin-top: 4px; letter-spacing: 0.3px; }

  /* business cards */
  .card { left: 66px; width: 170px; height: 94px; }
  .card-front { top: 696px; }
  .card-front .mark { right: 18px; top: 14px; gap: 4px; }
  .card-front .mark-dot { width: 18px; height: 18px; border-width: 2px; }
  .card-front .mark-name { font-size: 11px; }
  .card-front .mark-sub { font-size: 3.4px; margin-top: 1px; }
  .card-name { position: absolute; left: 17px; top: 55px; font-size: 5.2px; font-weight: 700; color: var(--brand-blue); }
  .card-role { position: absolute; left: 17px; top: 62px; font-size: 3.6px; }
  .card-rule { position: absolute; left: 17px; right: 16px; top: 67px; height: 0.6px; background: var(--rule); }
  .card-contact { position: absolute; left: 17px; top: 70px; font-size: 3.4px; line-height: 1.4; white-space: nowrap; }
  .card-contact b { color: var(--brand-green); font-weight: 600; }

  .card-back { top: 810px; background: var(--brand-blue); }
  .card-back .mark { left: 13px; top: 20px; }
  .card-back .mark-name { font-size: 17px; }
  .card-back .mark-sub { font-size: 5px; margin-top: 2px; }
  .card-band { position: absolute; left: 0; right: 0; top: 62px; height: 7px; background: var(--brand-green); font-size: 3.4px; color: var(--paper); padding-left: 13px; line-height: 7px; white-space: nowrap; }
  .card-web { position: absolute; left: 13px; top: 79px; font-size: 3.6px; color: var(--paper); }

  /* envelopes */
  .envelope { top: 696px; width: 415px; height: 208px; }
  .envelope-dl { left: 266px; }
  .envelope-dl .mark { left: 24px; top: 29px; gap: 7px; }
  .envelope-dl .mark-dot { width: 34px; height: 34px; }
  .envelope-dl .mark-name { font-size: 21px; }
  .envelope-dl .mark-sub { font-size: 5.4px; margin-top: 2px; }
  .envelope-address { position: absolute; left: 24px; top: 176px; font-size: 5.2px; line-height: 1.3; }

  .envelope-large { left: 718px; }
  .envelope-flap { position: absolute; left: 0; top: 0; width: 415px; height: 60px; }
  .flap-dot { position: absolute; left: 196px; top: 17px; width: 22px; height: 22px; border-radius: 50%; border: 2.5px solid var(--paper); }
</style>
</head>
<body>
<main class="canvas">

  <section class="sheet letterhead" aria-label="Letterhead">
    <div class="mark">
      <span class="mark-dot"></span>
      <span class="mark-text">
        <span class="mark-name">Vora Kest</span>
        <span class="mark-sub">Cleansers Trading L.L.C</span>
      </span>
    </div>
    <div class="partner-row">
      <span class="partner-badge green" role="img" aria-label="Partner badge"></span>
      <span class="partner-sep"></span>
      <span class="partner-badge red" role="img" aria-label="Partner badge"></span>
      <span class="partner-sep"></span>
      <span class="partner-badge navy" role="img" aria-label="Partner badge"></span>
      <span class="partner-sep"></span>
      <span class="partner-badge rose" role="img" aria-label="Membership badge"></span>
    </div>
    <div class="letterhead-rule"></div>
    <div class="letterhead-footer">
      <p>Ras Kulaib - Next to Nuwar Plaza Mall, Fanar Trade Tower - 614<br>
      <b>T:</b> 00971 4 57 86 204 - <b>F:</b> 00971 4 57 86 205 - <b>E:</b> info@vorakestclean.example</p>
      <p>www.vorakestclean.example</p>
    </div>
  </section>

  <section class="sheet folder on-blue" aria-label="Presentation folder">
    <div class="mark">
      <span class="mark-dot"></span>
      <span class="mark-text">
        <span class="mark-name">Vora Kest</span>
        <span class="mark-sub">Cleansers Trading L.L.C</span>
      </span>
    </div>
  </section>

  <section class="sheet card card-front" aria-label="Business card front">
    <div class="mark">
      <span class="mark-dot"></span>
      <span class="mark-text">
        <span class="mark-name">Vora Kest</span>
        <span class="mark-sub">Cleansers Trading L.L.C</span>
      </span>
    </div>
    <p class="card-name">Sami Yousef Hamdan Jaber</p>
    <p class="card-role">Director Manager</p>
    <div class="card-rule"></div>
    <p class="card-contact">Ras Kulaib - Next to Nuwar Plaza Mall, Fanar Trade Tower - 614<br>
      <b>T:</b> 00971 4 57 86 204 · <b>F:</b> 00971 4 57 86 205 · <b>E:</b> info@vorakestclean.example</p>
  </section>

  <section class="sheet card card-back on-blue" aria-label="Business card back">
    <div class="mark">
      <span class="mark-text">
        <span class="mark-name">Vora Kest</span>
        <span class="mark-sub">Cleansers Trading L.L.C</span>
      </span>
    </div>
    <p class="card-band">Home Care - Clean Supply - Trading</p>
    <p class="card-web">www.vorakestclean.example</p>
  </section>

  <section class="sheet envelope envelope-dl" aria-label="Small envelope">
    <div class="mark">
      <span class="mark-dot"></span>
      <span class="mark-text">
        <span class="mark-name">Vora Kest</span>
        <span class="mark-sub">Cleansers Trading L.L.C</span>
      </span>
    </div>
    <p class="envelope-address">Ras Kulaib - Next to Nuwar Plaza Mall<br>Fanar Trade Tower - 614<br>P.O.Box : 48207 Dubai - U.A.E</p>
  </section>

  <section class="sheet envelope envelope-large" aria-label="Large envelope">
    <svg class="envelope-flap" viewBox="0 0 415 60" aria-hidden="true">
      <path d="M0 0 H415 L408 48 Q406 58 396 58 H19 Q9 58 7 48 Z" fill="var(--brand-blue)"/>
    </svg>
    <span class="flap-dot"></span>
  </section>

</main>
</body>
</html>
```